Need Business Card for our Indian Grocery Store

Industry/Entity Type

Grocery Store

Contact Information for Business Card

Manoj Baweja
Director

Store Locations:

Kellbrook
482 Elm Parade
P: 03 9172 5843

Ashvale
613 Carlow Road
P: 03 9238 6014

email: kvtmarts@mailnest.example

Requirements
Must have
• Our logo Colours

```html
<!DOCTYPE html>
<html lang="en">
<head>
<meta charset="utf-8">
<title>KVT Marts Business Card</title>
<link rel="stylesheet" href="https://fonts.googleapis.com/css2?family=Roboto:wght@400;500;700&display=swap">
<style>
  :root {
    --backdrop: #3b3430;
    --card: #1d1f21;
    --card-edge: #2a2c2e;
    --brand-red: #e0201f;
    --silver: #a9abae;
    --silver-dim: #8a8c8f;
    --ink-light: #f2f2f2;
  }
  * { box-sizing: border-box; margin: 0; padding: 0; }
  html, body {
    width: 1200px; height: 769px; overflow: hidden;
    background: var(--backdrop);
    font-family: "Roboto", Arial, sans-serif;
  }
  .canvas { position: relative; width: 1200px; height: 769px; }
  .card {
    position: absolute; top: 241px;
    width: 500px; height: 286px;
    background: var(--card);
    border: 1px solid var(--card-edge);
    box-shadow: 0 12px 30px rgba(0,0,0,0.45);
  }
  .card-front { left: 60px; }
  .card-back { left: 640px; }

  .brand-name {
    position: absolute;
    font-family: "Roboto", Arial, sans-serif;
    font-weight: 700; letter-spacing: 2px; line-height: 1; white-space: nowrap;
  }
  .card-front .brand-name {
    left: 0; right: 0; top: 96px; text-align: center;
    color: var(--silver); font-size: 44px;
  }
  .card-back .brand-name {
    left: 16px; width: 240px; top: 124px; text-align: center;
    color: var(--brand-red); font-size: 36px;
  }

  .web-address {
    position: absolute; left: 0; right: 0; top: 176px; text-align: center;
    color: var(--silver-dim); font-size: 13px; letter-spacing: 4px;
  }

  .divider {
    position: absolute; left: 270px; top: 40px; width: 1px; height: 206px;
    background: linear-gradient(to bottom, transparent, #6a6c6f 50%, transparent);
  }

  .contact {
    position: absolute; left: 292px; top: 44px; width: 200px;
    color: var(--ink-light); font-size: 14px; line-height: 1.25;
  }
  .contact-name {
    color: var(--brand-red); font-weight: 700; font-size: 17px; text-transform: uppercase;
  }
  .contact-role { font-weight: 700; font-size: 14px; text-transform: uppercase; margin-bottom: 8px; }
  .store { margin-bottom: 8px; }
  .store b { font-weight: 700; }
  .online-line { display: flex; align-items: center; gap: 7px; font-size: 12.5px; white-space: nowrap; }
  .online-line svg { flex: none; }
</style>
</head>
<body>
<main class="canvas">
  <section class="card card-front" aria-label="Card front">
    <span class="brand-name">KVT MARTS</span>
    <p class="web-address">www.kvtmarts.example</p>
  </section>

  <section class="card card-back" aria-label="Card back">
    <span class="brand-name">KVT MARTS</span>
    <div class="divider"></div>
    <div class="contact">
      <p class="contact-name">Manoj Baweja</p>
      <p class="contact-role">Director</p>
      <p class="store">Kellbrook<br>482 Elm Parade<br><b>P</b> 03 9172 5843</p>
      <p class="store">Ashvale<br>613 Carlow Road<br><b>P</b> 03 9238 6014</p>
      <p class="online-line">
        <svg width="11" height="9" viewBox="0 0 11 9" aria-hidden="true"><rect width="11" height="9" rx="1" fill="#e0201f"/><path d="M0.5 1 L5.5 5 L10.5 1" stroke="#1d1f21" stroke-width="1.2" fill="none"/></svg>
        kvtmarts@mailnest.example
      </p>
      <p class="online-line">
        <svg width="11" height="11" viewBox="0 0 11 11" aria-hidden="true"><circle cx="5.5" cy="5.5" r="5.5" fill="#e0201f"/><path d="M0.5 5.5 H10.5 M5.5 0.5 C3 3 3 8 5.5 10.5 M5.5 0.5 C8 3 8 8 5.5 10.5" stroke="#1d1f21" stroke-width="0.9" fill="none"/></svg>
        www.kvtmarts.example
      </p>
    </div>
  </section>
</main>
</body>
</html>
```